Postcard Design for BQAV-

We need a postcard designed that is similar to our current example with information but has a few changes for the season. It needs to be an oversized postcard that meets KRTL BQAV requirements.

In the section that says complete car care, I'd like to add a blurb that Summer is here! Make sure your Car is ready and your:
AC is cold
Cooling system is functioning properly
Tires and Alighment are vacation ready

Elsewhere on the card, we need to add that we offer a 3 year/36,000 warranty on parts and labor

We also need to add that we have a 5.0 Zorvia Review Score and a 4.9 Pavo Nimbal score

Colors can change as can font as long as it is easy to read

```html
<!DOCTYPE html>
<html lang="en">
<head>
<meta charset="utf-8">
<title>Copper Lane Automotive Repair – Postcard</title>
<link rel="stylesheet" href="https://fonts.googleapis.com/css2?family=Archivo+Black&family=Montserrat:wght@500;600;700;800&display=swap">
<style>
  :root{
    --blue:#0f9fe0;
    --green:#78b236;
    --ink:#111111;
    --paper:#ffffff;
    --paper-soft:#f3f4f5;
    --stage:#858585;
    --rule:#9a9a9a;
    --star:#f5b400;
  }
  *{box-sizing:border-box;margin:0;padding:0}
  html,body{width:1200px;height:900px;overflow:hidden}
  body{background:var(--stage);font-family:"Montserrat",Arial,sans-serif;color:var(--ink);position:relative}

  .card{position:absolute;width:615px;height:410px;background:var(--paper);overflow:hidden;box-shadow:0 6px 14px rgba(0,0,0,.35)}
  .card--front{left:60px;top:25px}
  .card--back{left:525px;top:465px}

  /* ---------- front ---------- */
  .front-photo{position:absolute;left:0;top:0;width:615px;height:330px;
    background:linear-gradient(100deg,#f1f3f4 0%,#e4ecf0 30%,#a9cde0 50%,#5f93b8 68%,#3b6386 84%,#2b4862 100%)}
  .brand{position:absolute;font-family:"Montserrat",Arial,sans-serif;font-weight:700;color:var(--ink);text-transform:uppercase;line-height:1.05}
  .brand__mark{display:inline-block;width:14px;height:14px;border-radius:50%;background:var(--ink);vertical-align:middle;margin-right:8px}
  .front .brand{left:24px;top:118px;font-size:15px;letter-spacing:.5px}
  .front .brand small{display:block;font-size:10px;margin-left:22px;letter-spacing:1px}

  .offer-burst{position:absolute;left:268px;top:34px;width:160px;height:160px}
  .offer-burst p{position:absolute;inset:0;display:flex;align-items:center;justify-content:center;text-align:center;
    color:#fff;font-weight:800;font-size:11.5px;line-height:1.2;text-transform:uppercase;padding:0 22px}

  .headline{position:absolute;left:24px;top:170px}
  .headline__kicker{font-family:"Archivo Black",Arial,sans-serif;font-size:22px;line-height:1}
  .headline__main{font-family:"Archivo Black",Arial,sans-serif;font-size:62px;line-height:.88;letter-spacing:-1px}
  .headline__sub{font-weight:800;font-size:18px;margin-top:4px}

  .trust-panel{position:absolute;left:392px;top:206px;width:206px;background:var(--paper);border-radius:4px;
    box-shadow:0 3px 8px rgba(0,0,0,.3);overflow:hidden}
  .trust-panel__warranty{background:var(--green);color:#fff;padding:7px 10px;text-align:center}
  .trust-panel__warranty strong{display:block;font-family:"Archivo Black",Arial,sans-serif;font-size:14px;line-height:1.1;font-weight:400}
  .trust-panel__warranty span{display:block;font-weight:700;font-size:9.5px;line-height:1.3;text-transform:uppercase}
  .rating{display:flex;align-items:center;gap:7px;padding:5px 10px}
  .rating + .rating{border-top:1px solid #e2e2e2}
  .rating__score{font-family:"Archivo Black",Arial,sans-serif;font-size:18px;line-height:1;color:var(--blue)}
  .rating__text{font-weight:700;font-size:9.5px;line-height:1.2}
  .rating__stars{display:flex;gap:1px;margin-top:2px}
  .rating__stars svg{width:9px;height:9px}

  .band{position:absolute;left:0;bottom:0;width:100%;height:80px;background:var(--blue)}
  .band__call{position:absolute;left:0;top:0;height:100%;width:300px;background:var(--green);
    clip-path:polygon(0 0,100% 0,92% 100%,0 100%);padding:14px 0 0 22px}
  .call-label{font-family:"Archivo Black",Arial,sans-serif;font-size:22px;line-height:1;color:var(--ink)}
  .call-number{font-family:"Archivo Black",Arial,sans-serif;font-size:24px;line-height:1.1;color:#fff;display:flex;align-items:center;gap:6px}
  .call-number svg{width:18px;height:18px}
  .band__contact{position:absolute;left:310px;top:12px;color:#fff;font-weight:600;font-size:12px;line-height:1.85}
  .band__contact li{list-style:none;display:flex;align-items:center;gap:6px}
  .band__contact svg{width:13px;height:13px;flex:none}

  /* ---------- back ---------- */
  .ad{position:absolute;left:0;top:0;width:330px;height:410px;background:var(--paper-soft)}
  .ad__divider{position:absolute;left:330px;top:0;width:6px;height:410px;background:var(--green)}
  .ad__title{position:absolute;left:0;top:0;width:100%;height:100px;background:var(--blue);color:#fff;padding:14px 0 0 20px}
  .ad__title .kicker{font-family:"Archivo Black",Arial,sans-serif;font-size:22px;line-height:1}
  .ad__title .main{font-family:"Archivo Black",Arial,sans-serif;font-size:48px;line-height:1}
  .ad__intro{position:absolute;left:0;top:100px;width:100%;padding:6px 16px 0 20px;background:#fff;height:60px}
  .ad__intro h2{font-weight:800;font-size:15.5px;line-height:1.1}
  .ad__intro p{font-weight:600;font-size:7.6px;line-height:1.3;margin-top:3px}
  .summer{position:absolute;left:0;top:160px;width:100%;height:74px;background:var(--paper-soft);padding:7px 16px 0 20px;border-top:3px solid var(--green)}
  .summer h3{font-family:"Archivo Black",Arial,sans-serif;font-weight:400;font-size:11.5px;line-height:1.15;color:var(--blue)}
  .summer h3 span{font-family:"Montserrat",Arial,sans-serif;font-weight:700;font-size:8.5px;color:var(--ink)}
  .summer ul{list-style:none;margin-top:4px}
  .summer li{display:flex;align-items:center;gap:5px;font-weight:700;font-size:8.5px;line-height:1.45}
  .summer li svg{width:9px;height:9px;flex:none}
  .ad__photo{position:absolute;left:0;top:234px;width:100%;height:64px;
    background:linear-gradient(110deg,#c9d3da 0%,#6f7f8c 40%,#3a4652 65%,#a9b8c4 100%)}
  .ad__perks{position:absolute;left:0;top:298px;width:100%;height:44px;background:#fff;display:flex;align-items:center;justify-content:space-between;padding:0 12px}
  .perk{display:flex;align-items:center;gap:6px;font-weight:600;font-size:8.3px;line-height:1.25;width:150px}
  .perk svg{width:18px;height:18px;flex:none}
  .ad .band{height:68px}
  .ad .band__call{width:150px;padding:12px 0 0 14px}
  .ad .call-label{font-size:15px}
  .ad .call-number{font-size:15px}
  .ad .call-number svg{width:12px;height:12px}
  .ad .band__contact{left:160px;top:14px;font-size:9.5px;line-height:2}
  .ad .band__contact svg{width:10px;height:10px}

  .mailing{position:absolute;left:336px;top:0;width:279px;height:410px;background:var(--paper)}
  .indicia{position:absolute;right:18px;top:18px;width:78px;border:1px solid var(--rule);padding:5px 4px;text-align:center;font-weight:700;font-size:6px;line-height:1.35;text-transform:uppercase}
  .mailing .brand{left:22px;top:92px;font-size:13px}
  .mailing .brand small{display:block;font-size:8.5px;margin-left:22px;letter-spacing:.8px}
  .return-address{position:absolute;left:22px;top:130px;font-weight:500;font-size:7.2px;line-height:1.35}
  .address-box{position:absolute;left:22px;top:168px;width:235px;height:64px;border:1px solid var(--rule);padding:10px 12px;font-weight:600;font-size:7.2px;line-height:1.8}
</style>
</head>
<body>

<!-- Front side -->
<section class="card card--front front">
  <div class="front-photo" role="img" aria-label="Photo of a mechanic in overalls inspecting a car engine in a bright workshop"></div>

  <div class="brand"><span class="brand__mark"></span>Copper Lane<small>Automotive Repair</small></div>

  <div class="offer-burst">
    <svg viewBox="0 0 100 100" width="160" height="160" aria-hidden="true">
      <polygon fill="#0f9fe0" points="50,2 56,13 67,5 69,18 82,14 79,27 93,29 85,39 97,46 87,54 96,63 83,67 88,80 75,79 74,93 62,87 56,98 49,89 41,98 36,87 24,93 23,79 10,80 15,67 3,63 12,54 3,46 14,39 7,29 20,27 17,14 30,18 32,5 43,13"/>
    </svg>
    <p>Free vehicle pick up, drop off, &amp; loaners</p>
  </div>

  <div class="headline">
    <div class="headline__kicker">HIGH-QUALITY</div>
    <div class="headline__main">AUTO<br>REPAIR</div>
    <div class="headline__sub">&amp; Preventative maintenance</div>
  </div>

  <aside class="trust-panel">
    <div class="trust-panel__warranty">
      <strong>3 YEAR / 36,000 MILE</strong>
      <span>Warranty on parts &amp; labor</span>
    </div>
    <div class="rating">
      <div class="rating__score">5.0</div>
      <div>
        <div class="rating__text">Zorvia Review Score</div>
        <div class="rating__stars" aria-hidden="true">
          <svg viewBox="0 0 24 24"><path fill="#f5b400" d="M12 2l3 7h7l-5.5 4.5L18.5 21 12 16.8 5.5 21l2-7.5L2 9h7z"/></svg>
          <svg viewBox="0 0 24 24"><path fill="#f5b400" d="M12 2l3 7h7l-5.5 4.5L18.5 21 12 16.8 5.5 21l2-7.5L2 9h7z"/></svg>
          <svg viewBox="0 0 24 24"><path fill="#f5b400" d="M12 2l3 7h7l-5.5 4.5L18.5 21 12 16.8 5.5 21l2-7.5L2 9h7z"/></svg>
          <svg viewBox="0 0 24 24"><path fill="#f5b400" d="M12 2l3 7h7l-5.5 4.5L18.5 21 12 16.8 5.5 21l2-7.5L2 9h7z"/></svg>
          <svg viewBox="0 0 24 24"><path fill="#f5b400" d="M12 2l3 7h7l-5.5 4.5L18.5 21 12 16.8 5.5 21l2-7.5L2 9h7z"/></svg>
        </div>
      </div>
    </div>
    <div class="rating">
      <div class="rating__score">4.9</div>
      <div>
        <div class="rating__text">Pavo Nimbal Score</div>
        <div class="rating__stars" aria-hidden="true">
          <svg viewBox="0 0 24 24"><path fill="#f5b400" d="M12 2l3 7h7l-5.5 4.5L18.5 21 12 16.8 5.5 21l2-7.5L2 9h7z"/></svg>
          <svg viewBox="0 0 24 24"><path fill="#f5b400" d="M12 2l3 7h7l-5.5 4.5L18.5 21 12 16.8 5.5 21l2-7.5L2 9h7z"/></svg>
          <svg viewBox="0 0 24 24"><path fill="#f5b400" d="M12 2l3 7h7l-5.5 4.5L18.5 21 12 16.8 5.5 21l2-7.5L2 9h7z"/></svg>
          <svg viewBox="0 0 24 24"><path fill="#f5b400" d="M12 2l3 7h7l-5.5 4.5L18.5 21 12 16.8 5.5 21l2-7.5L2 9h7z"/></svg>
          <svg viewBox="0 0 24 24"><path fill="#f5b400" d="M12 2l3 7h7l-5.5 4.5L18.5 21 12 16.8 5.5 21l2-7.5L2 9h7z"/></svg>
        </div>
      </div>
    </div>
  </aside>

  <div class="band">
    <div class="band__call">
      <div class="call-label">CALL US TODAY</div>
      <div class="call-number">
        <svg viewBox="0 0 24 24" aria-hidden="true"><circle cx="12" cy="12" r="12" fill="#111"/><path fill="#fff" d="M8.5 6.5l2 2-1.2 1.6c.7 1.6 1.9 2.8 3.5 3.5l1.6-1.2 2 2-1.4 2.1c-4.4-.5-8-4.1-8.5-8.5z"/></svg>
        610-555-0182
      </div>
    </div>
    <ul class="band__contact">
      <li><svg viewBox="0 0 24 24" aria-hidden="true"><circle cx="12" cy="12" r="12" fill="#111"/><path fill="#fff" d="M12 5a4.5 4.5 0 0 0-4.5 4.5c0 3.3 4.5 9 4.5 9s4.5-5.7 4.5-9A4.5 4.5 0 0 0 12 5zm0 6.2a1.7 1.7 0 1 1 0-3.4 1.7 1.7 0 0 1 0 3.4z"/></svg>218 Willowmere Road, Unit B, Elm Hollow</li>
      <li><svg viewBox="0 0 24 24" aria-hidden="true"><circle cx="12" cy="12" r="12" fill="#111"/><rect x="6" y="8" width="12" height="8" fill="#fff"/><path d="M6 8l6 5 6-5" stroke="#111" stroke-width="1.2" fill="none"/></svg>info@copperlanerepair.com</li>
      <li><svg viewBox="0 0 24 24" aria-hidden="true"><circle cx="12" cy="12" r="12" fill="#111"/><circle cx="12" cy="12" r="6" fill="none" stroke="#fff" stroke-width="1.3"/><path d="M6 12h12M12 6c-2.5 3-2.5 9 0 12M12 6c2.5 3 2.5 9 0 12" stroke="#fff" stroke-width="1.1" fill="none"/></svg>www.copperlanerepair.com</li>
    </ul>
  </div>
</section>

<!-- Mailing side -->
<section class="card card--back">
  <div class="ad">
    <div class="ad__title">
      <div class="kicker">COMPLETE</div>
      <div class="main">CAR CARE</div>
    </div>
    <div class="ad__intro">
      <h2>Including inspections &amp; emissions</h2>
      <p>Dont trust your car to just any automotive repair shop. We have the reliable, experienced technicians to quickly diagnose whats wrong &amp; fix it right the first time— saving you time, headaches &amp; money.</p>
    </div>
    <div class="summer">
      <h3>SUMMER IS HERE! <span>Make sure your car is ready and your:</span></h3>
      <ul>
        <li><svg viewBox="0 0 24 24" aria-hidden="true"><circle cx="12" cy="12" r="12" fill="#78b236"/><path d="M6.5 12.5l3.5 3.5 7.5-8" stroke="#fff" stroke-width="2.6" fill="none"/></svg>AC is cold</li>
        <li><svg viewBox="0 0 24 24" aria-hidden="true"><circle cx="12" cy="12" r="12" fill="#78b236"/><path d="M6.5 12.5l3.5 3.5 7.5-8" stroke="#fff" stroke-width="2.6" fill="none"/></svg>Cooling system is functioning properly</li>
        <li><svg viewBox="0 0 24 24" aria-hidden="true"><circle cx="12" cy="12" r="12" fill="#78b236"/><path d="M6.5 12.5l3.5 3.5 7.5-8" stroke="#fff" stroke-width="2.6" fill="none"/></svg>Tires and alignment are vacation ready</li>
      </ul>
    </div>
    <div class="ad__photo" role="img" aria-label="Photo of a technician leaning over an open car engine with a laptop on the fender"></div>
    <div class="ad__perks">
      <div class="perk">
        <svg viewBox="0 0 24 24" aria-hidden="true"><path fill="#78b236" d="M3 10l9-6 9 6v10h-3v-8H6v8H3z"/><rect x="8" y="14" width="8" height="4" rx="1" fill="#78b236"/></svg>
        Trust in a timely, full-service repair facility.
      </div>
      <div class="perk">
        <svg viewBox="0 0 24 24" aria-hidden="true"><path fill="#78b236" d="M4 5h16v10H10l-5 4v-4H4z"/><circle cx="9" cy="10" r="1.2" fill="#fff"/><circle cx="12" cy="10" r="1.2" fill="#fff"/><circle cx="15" cy="10" r="1.2" fill="#fff"/></svg>
        Enjoy unparalleled Customer service
      </div>
    </div>
    <div class="band">
      <div class="band__call">
        <div class="call-label">CALL US TODAY</div>
        <div class="call-number">
          <svg viewBox="0 0 24 24" aria-hidden="true"><circle cx="12" cy="12" r="12" fill="#111"/><path fill="#fff" d="M8.5 6.5l2 2-1.2 1.6c.7 1.6 1.9 2.8 3.5 3.5l1.6-1.2 2 2-1.4 2.1c-4.4-.5-8-4.1-8.5-8.5z"/></svg>
          610-555-0182
        </div>
      </div>
      <ul class="band__contact">
        <li><svg viewBox="0 0 24 24" aria-hidden="true"><circle cx="12" cy="12" r="12" fill="#111"/><rect x="6" y="8" width="12" height="8" fill="#fff"/><path d="M6 8l6 5 6-5" stroke="#111" stroke-width="1.2" fill="none"/></svg>info@copperlanerepair.com</li>
        <li><svg viewBox="0 0 24 24" aria-hidden="true"><circle cx="12" cy="12" r="12" fill="#111"/><circle cx="12" cy="12" r="6" fill="none" stroke="#fff" stroke-width="1.3"/><path d="M6 12h12M12 6c-2.5 3-2.5 9 0 12M12 6c2.5 3 2.5 9 0 12" stroke="#fff" stroke-width="1.1" fill="none"/></svg>www.copperlanerepair.com</li>
      </ul>
    </div>
  </div>
  <div class="ad__divider"></div>

  <div class="mailing">
    <div class="indicia">PRSRT STD<br>ECRWSS<br>U.S. Postage<br>Paid<br>BQAV Retail</div>
    <div class="brand"><span class="brand__mark"></span>Copper Lane<small>Automotive Repair</small></div>
    <div class="return-address">Copper Lane Repair 218 Willowmere Road,<br>Unit B, Elm Hollow, PA 17000</div>
    <div class="address-box">***************ECRWSS****<br>Local Postal Customer</div>
  </div>
</section>

</body>
</html>
```